Lorvel MediSpa - Mailchimp Email

I have a list of prospects that I want to email. I'm using Mailchimp. I would like my template to explain that we are now open and ready for business. We are offering 20% off on all services and special procedure combination deals. I want the design to be a template that I can use the same look and feel for future emails - for information giving, beauty tips. monthly promos, etc.

I don't know much about email campaigns, but I'd like to keep it simple, let the people know we're open for business and try to get them to either respond to the email or call for a free consult.
Updates

Thank you all for your hard work on my project.

Target Market(s)

The list criteria is female, income greater than $50,000, between the age of 30 and 65. The area is affluent - Potomac, Bethesda and Chevy Chase Maryland

Industry/Entity Type

Health And Wellness

Font styles to use
Other font styles liked:
• I'd like to keep the font simple like our logo font - again if possible.

Colors

Designer to choose colors to be used in the design.

Requirements
Must have
• my logo, nice pictures related to the medispa business, location "1 block from Brackenridge Harlow Mall', link to our website
Nice to have
• place to input their info to sign up for future emails - i see this on websites. I don't know if they do this for emails. Mailchimp seems to use them.
• Keep the look and feel of our website if that makes sense - www.lorvelmedispa-example.com.
Should not have
• don't be too busy or too long. Keep it simple if possible.

```html
<!DOCTYPE html>
<html lang="en">
<head>
<meta charset="utf-8">
<title>Lorvel MediSpa – Now Open</title>
<link rel="stylesheet" href="https://fonts.googleapis.com/css2?family=Raleway:wght@300;400;500;600;700&display=swap">
<style>
:root{
  --green:#7cbd2c;
  --green-dark:#6aa822;
  --ink:#333333;
  --muted:#8a8a8a;
  --soft-bg:#f8f8f8;
  --line:#e2e2e2;
  --button-grey:#9d9d9d;
  --footer-bar:#262626;
  --white:#ffffff;
}
*{box-sizing:border-box;margin:0;padding:0}
html,body{width:1200px;height:3701px;overflow:hidden;background:var(--white)}
body{font-family:'Raleway',sans-serif;color:var(--ink);position:relative}
.section{position:absolute;left:0;width:1200px}
.center{text-align:center}

/* header */
.site-header{top:0;height:136px;background:var(--white)}
.brand{position:absolute;left:175px;top:34px;display:flex;align-items:center;gap:14px}
.brand-dot{width:68px;height:68px;border-radius:50%;background:var(--ink)}
.brand-name{font-size:34px;font-weight:600;color:var(--ink);line-height:1}
.nav{position:absolute;right:170px;top:58px;display:flex;gap:44px;font-size:21px;color:#555}

/* hero */
.hero{top:136px;height:506px;background:linear-gradient(100deg,#6f7a5c 0%,#a79887 45%,#caa894 70%,#7b6a5e 100%)}
.hero-photo{position:absolute;inset:0}
.hero-title{position:absolute;top:372px;width:100%;font-size:55px;font-weight:300;color:var(--white);top:236px}
.hero-btn{position:absolute;left:425px;top:365px;width:350px;height:67px;border-radius:34px;background:var(--green);color:var(--white);font-size:25px;font-weight:500;display:flex;align-items:center;justify-content:center;gap:12px}

/* intro */
.intro{top:642px;height:326px;background:var(--soft-bg)}
.intro-title{margin-top:52px;font-size:42px;font-weight:500;color:var(--green);letter-spacing:1px}
.intro-sub{margin-top:6px;font-size:19px;color:var(--muted)}
.intro-text{margin:20px auto 0;width:830px;font-size:19px;line-height:30px;color:#999}
.read-more{margin-top:10px;font-size:16px;letter-spacing:1px;color:var(--green);font-weight:500}

/* services */
.services{top:968px;height:1020px;background:var(--white)}
.section-title{font-size:32px;font-weight:500;color:var(--green)}
.services .section-title{position:absolute;top:58px;width:100%}
.service{position:absolute;width:395px}
.service-photo{width:395px;height:222px}
.service-name{margin-top:36px;font-size:30px;font-weight:500;color:var(--green);letter-spacing:.5px}
.service-desc{margin-top:6px;font-size:17px;line-height:24px;color:var(--muted)}
.service-link{margin-top:6px;font-size:21px;color:var(--green)}

/* testimonials */
.testimonials{top:1988px;height:644px;background:var(--soft-bg)}
.testimonials .section-title{position:absolute;top:52px;width:100%;font-size:29px}
.quote-card{position:absolute;top:118px;width:395px;height:304px;border:1px solid var(--line);background:var(--white);padding:24px 30px;text-align:center}
.quote-head{font-size:18px;font-weight:500;color:var(--green)}
.quote-body{margin-top:6px;font-size:17px;line-height:29px;color:#888}
.reviewer{position:absolute;top:458px;width:395px;text-align:center}
.avatar{width:90px;height:90px;border-radius:50%;margin:0 auto}
.reviewer-name{margin-top:30px;font-size:20px;font-weight:600;color:#555}

/* coupons & cta */
.offers{top:2632px;height:738px;background:var(--white)}
.offers .section-title{position:absolute;top:50px;width:100%;font-size:30px}
.coupon{position:absolute;top:133px;width:390px;height:238px;border:4px dotted var(--green);text-align:center;padding-top:20px}
.coupon-date{font-size:23px;color:var(--green);font-weight:500}
.coupon-value{font-size:58px;font-weight:500;color:var(--green);line-height:1.05}
.coupon-terms{margin:6px auto 0;width:340px;font-size:16px;line-height:22px;color:#888}
.divider{position:absolute;left:86px;top:416px;width:993px;height:2px;background:var(--line)}
.tagline{position:absolute;top:454px;width:100%;font-size:31px;line-height:44px;color:#777}
.tagline strong{color:var(--green);font-weight:500}
.appointments{position:absolute;top:560px;width:100%;font-size:30px;font-weight:600;color:var(--green);letter-spacing:.5px}
.signup-btn{position:absolute;left:437px;top:627px;width:323px;height:69px;background:var(--button-grey);color:var(--white);font-size:25px;font-weight:600;display:flex;align-items:center;justify-content:center;letter-spacing:.5px}

/* footer */
.site-footer{top:3370px;height:257px;background:var(--green)}
.footer-brand{position:absolute;top:48px;left:0;width:100%;display:flex;justify-content:center;align-items:center;gap:16px}
.footer-brand .brand-dot{width:90px;height:90px;background:var(--white)}
.footer-brand .brand-name{color:var(--white);font-size:42px}
.footer-address{position:absolute;top:180px;width:100%;font-size:20px;color:var(--white)}
.footer-bar{top:3627px;height:74px;background:var(--footer-bar);color:var(--white);font-size:16px}
.social{position:absolute;left:40px;top:25px;display:flex;align-items:center;gap:12px}
.social-dot{width:24px;height:24px;border-radius:50%;border:2px solid var(--green)}
.copyright{position:absolute;right:40px;top:27px}
</style>
</head>
<body>

<header class="section site-header">
  <div class="brand"><span class="brand-dot"></span><span class="brand-name">Lorvel MediSpa</span></div>
  <nav class="nav"><span>Our Servies</span><span>Features</span><span>Pricing</span><span>Contact</span></nav>
</header>

<section class="section hero">
  <div class="hero-photo" role="img" aria-label="Photo of a woman with clear skin resting her chin on her hand, soft green foliage behind"></div>
  <h1 class="hero-title center">Follow Us to an Improved You</h1>
  <div class="hero-btn">Get It Now
    <svg width="24" height="14" viewBox="0 0 24 14"><path d="M1 7h20M15 1l6 6-6 6" fill="none" stroke="#fff" stroke-width="2"/></svg>
  </div>
</section>

<section class="section intro center">
  <h2 class="intro-title">EVERYTHING YOU NEED TO</h2>
  <p class="intro-sub">Rejuvenate &amp; Revitalize</p>
  <p class="intro-text">Our goals are natural beauty and patient satisfaction. We strive to make sure you are happy with your look. We are committed to enhance your natural beauty.</p>
  <p class="read-more">READ MORE
    <svg width="20" height="12" viewBox="0 0 20 12"><path d="M1 6h16M12 1l5 5-5 5" fill="none" stroke="#7cbd2c" stroke-width="1.8"/></svg>
  </p>
</section>

<section class="section services">
  <h2 class="section-title center">Our Services</h2>

  <article class="service" style="left:175px;top:136px">
    <div class="service-photo" role="img" aria-label="Photo of a relaxed woman receiving a gentle facial massage" style="background:linear-gradient(120deg,#c9a08a,#8a5d4b)"></div>
    <h3 class="service-name">FACIAL ASTHETICS</h3>
    <p class="service-desc">Dermal Fillers, Neuvara, Toxelle Cosmetic<br>Lumafill, Densiva, Chinova,<br>PRP Injections</p>
    <p class="service-link">Read More..</p>
  </article>

  <article class="service" style="left:627px;top:136px">
    <div class="service-photo" role="img" aria-label="Photo of hands applying treatment to a client's shoulder" style="background:linear-gradient(120deg,#e6cbb8,#b88a74)"></div>
    <h3 class="service-name">LASER SKIN TREATMENT</h3>
    <p class="service-desc">Skin Revitalization, Q18™ Laser Treatments<br>Vascular Treatments, Scars, Stretch Marks<br>Tattoo Removal Brightwave Laser Hair Removal</p>
    <p class="service-link">Read More..</p>
  </article>

  <article class="service" style="left:175px;top:587px">
    <div class="service-photo" role="img" aria-label="Photo of a toned torso under an open white shirt" style="background:linear-gradient(90deg,#f0efed 0%,#b07a5e 30%,#8e5c44 70%,#ece9e6 100%)"></div>
    <h3 class="service-name">BODY CONTOURING</h3>
    <p class="service-desc">Skin Tightening, Cellulite Reduction<br>Medically Supervised Weight<br>Loss Program</p>
    <p class="service-link">Read More..</p>
  </article>

  <article class="service" style="left:627px;top:587px">
    <div class="service-photo" role="img" aria-label="Photo of a gloved practitioner performing a laser treatment on a client's face" style="background:linear-gradient(120deg,#8f8a78,#c6b09c 55%,#e2d6c8)"></div>
    <h3 class="service-name">LASER SKIN TREATMENT</h3>
    <p class="service-desc">The ClearGlide by Brightwave laser hair removal<br>features a patented cooling system that helps<br>protect the skin</p>
    <p class="service-link">Read More..</p>
  </article>
</section>

<section class="section testimonials">
  <h2 class="section-title center">Our Testimonials</h2>

  <blockquote class="quote-card" style="left:175px">
    <p class="quote-head">I strongly recommend</p>
    <p class="quote-body">As a professional working Mom, I highly value quality service and time. Dr. Halvorsen and Maribel consistently provide both. As my primary doctor, Dr. Halvorsen really listens to me as his patient. Maribel provides that personal touch and always strives to make sure I leave satisfied with my treatments.</p>
  </blockquote>
  <blockquote class="quote-card" style="left:627px">
    <p class="quote-head">I am very happy with the outcome</p>
    <p class="quote-body">As a professional working Mom, I highly value quality service and time. Dr. Halvorsen and Maribel consistently provide both. As my primary doctor, Dr. Halvorsen really listens to me as his patient. Maribel provides that personal touch and always strives to make sure I leave satisfied with my treatments.</p>
  </blockquote>

  <div class="reviewer" style="left:175px">
    <div class="avatar" role="img" aria-label="Reviewer portrait" style="background:radial-gradient(circle,#d9c2ae,#6b6358)"></div>
    <p class="reviewer-name">- Renata P.</p>
  </div>
  <div class="reviewer" style="left:627px">
    <div class="avatar" role="img" aria-label="Reviewer portrait" style="background:radial-gradient(circle,#f0d6a8,#c99c5a)"></div>
    <p class="reviewer-name">Jolene Marsh</p>
  </div>
</section>

<section class="section offers">
  <h2 class="section-title center">Our Offer Coupons</h2>

  <div class="coupon" style="left:180px">
    <p class="coupon-date">Expiration Date : 6/3/2019</p>
    <p class="coupon-value">20% Off</p>
    <p class="coupon-terms">All injectable and mediaspa services. Skin care products not eligible with this promotion. canot comible the other promotional or package prices</p>
  </div>
  <div class="coupon" style="left:630px">
    <p class="coupon-date">Expiration Date : 6/3/2019</p>
    <p class="coupon-value">20% Off</p>
    <p class="coupon-terms">All injectable and mediaspa services. Skin care products not eligible with this promotion. canot comible the other promotional or package prices</p>
  </div>

  <div class="divider"></div>
  <p class="tagline center"><strong>The outside</strong> can only shine if <strong style="font-weight:600">the inside</strong> is working<br>the way it is supposed to.</p>
  <p class="appointments center">APPOINTMENTS : 240.555.0142</p>
  <div class="signup-btn">SIGN UP NOW</div>
</section>

<footer class="section site-footer">
  <div class="footer-brand"><span class="brand-dot"></span><span class="brand-name">Lorvel MediSpa</span></div>
  <p class="footer-address center">4210 Alder Crest Blvd. Suite B-208, Bethesda, MD 20817</p>
</footer>

<div class="section footer-bar">
  <div class="social">FOLLOW US ON SOCIAL MEDIA <span class="social-dot"></span><span class="social-dot"></span><span class="social-dot"></span></div>
  <div class="copyright">© 2019 lorvel medispa. All Rights Reserved</div>
</div>

</body>
</html>
```